Quiet Harbor Path - Web design

I require a complete design for a responsive 3 page business website.

High end design type, similar to (in order of preference):
]https://brennaolstead.co/
https://riverstone-guidance-wellbeing.com.au/
https://calmridgementoring.com.au/
https://buildyourglow.com/
https://theclearpathguide.com/
https://www.dervlakempson.com/
https://theloom.com/

Please use the attached old company logo, which is to be used a reference for the new branding and design.

Please use the colour palette below
#3D3D3D
#FBF8F3
#CAAD53
#7EB492
#EDCFBF

Target Market(s)

Male & female 30-50s, small business owners and executive corporates, first world english speaking nations.

Industry/Entity Type

Life Coaching

Logo Text

Quiet Harbor Path. Tagline: Holistic Transformational Coaching

Number of Pages Required

3 page

Font styles to use
Sans Serif

Requirements
Must have
• Testimonials section, google reivews section, book online button.

```html
<!DOCTYPE html>
<html lang="en">
<head>
<meta charset="utf-8">
<title>Everbloom — Holistic Transformational Coaching</title>
<link rel="stylesheet" href="https://fonts.googleapis.com/css2?family=Josefin+Sans:wght@300;400;600;700&display=swap">
<style>
:root{
  --dark:#3D3D3D;
  --cream:#FBF8F3;
  --gold:#CAAD53;
  --green:#7EB492;
  --peach:#EDCFBF;
  --muted:#9a9a9a;
  --line:#e3e3e3;
  --white:#ffffff;
}
*{box-sizing:border-box}
html,body{margin:0;padding:0}
body{width:1200px;height:5372px;overflow:hidden;background:var(--white);font-family:"Josefin Sans",sans-serif;color:var(--dark);position:relative}
.abs{position:absolute}
section,header,footer{position:absolute;left:0;width:1200px}
p{margin:0}
h1,h2,h3,h4{margin:0;font-weight:400}
.btn{position:absolute;display:flex;align-items:center;justify-content:center;gap:8px;border-radius:30px;font-size:13px;color:var(--white);background:var(--green);height:58px}
.btn-ghost{background:transparent;border:2px solid var(--white)}
.section-title{position:absolute;color:var(--gold);font-size:34px;font-weight:600}
.center{text-align:center;left:0;width:1200px}

/* header */
.site-header{top:0;height:98px;background:#f3ede3}
.brand{left:184px;top:30px;display:flex;flex-direction:column;align-items:center;gap:6px}
.brand-name{font-size:18px;letter-spacing:1px;color:#8a7a60}
.brand-mark{width:12px;height:12px;border-radius:50%;background:var(--green)}
.nav{top:50px;font-size:13px;color:var(--dark)}
.nav.active{color:var(--green)}

/* hero */
.hero{top:98px;height:476px;background:linear-gradient(180deg,#f0a23a 0%,#e3862a 40%,#b8581a 70%,#6e3314 100%)}
.hero h1{position:absolute;top:95px;left:0;width:1200px;text-align:center;color:var(--white);font-size:46px;line-height:57px;font-weight:400}
.hero p{position:absolute;top:232px;left:250px;width:700px;text-align:center;color:var(--white);font-size:13px;line-height:25px}

/* partners */
.partners{top:660px;height:70px;display:flex;align-items:center;justify-content:space-between;padding:0 184px}
.partner{font-size:16px;color:#c6c6c6;font-weight:600}
.partner-sq{width:22px;height:22px;background:#d6d6d6}

/* about */
.about{top:740px;height:560px}
.about-frame{left:159px;top:80px;width:390px;height:445px;border:11px solid var(--peach)}
.about-photo{left:250px;top:18px;width:199px;height:494px;background:linear-gradient(180deg,#e9e6e3 0%,#d9d6d2 45%,#5a5e66 70%,#4a4d54 100%);border-radius:100px 100px 0 0}
.about h2{left:611px;top:130px;color:var(--gold);font-size:34px;font-weight:600}
.about .lead{left:611px;top:200px;width:370px;font-size:13px;line-height:25px}
.about .body{left:611px;top:258px;width:385px;font-size:13px;line-height:25px;color:var(--muted)}

/* booking */
.booking{top:1357px;height:333px;background:linear-gradient(90deg,#3a2613 0%,#7a5327 35%,#a57a3f 60%,#5a3b1c 100%)}
.booking p{position:absolute;top:80px;left:150px;width:900px;text-align:center;color:var(--white);font-size:28px;line-height:39px}

/* services */
.services{top:1700px;height:640px}
.services .section-title{left:184px;top:78px}
.services .intro{position:absolute;left:184px;top:150px;width:500px;font-size:13px;line-height:25px}
.arrow-btn{position:absolute;width:38px;height:38px;border-radius:50%;display:flex;align-items:center;justify-content:center}
.arrow-btn.off{background:#f6f3ee}
.arrow-btn.on{background:var(--green)}
.service-card{position:absolute;top:232px;width:262px;text-align:center}
.service-card .thumb{height:172px}
.service-card h3{margin-top:24px;font-size:14px;font-weight:600}
.service-card p{margin-top:14px;font-size:13px;line-height:25px;color:var(--muted);padding:0 12px}
.learn{margin-top:12px;font-size:12px;color:var(--peach);display:flex;justify-content:center;gap:6px}
.learn.on{color:var(--green)}

/* events */
.events{top:2344px;height:970px;background:var(--cream)}
.events .section-title{top:75px}
.event-feature{left:184px;top:194px;width:546px;height:317px;background:linear-gradient(160deg,#6b4a44 0%,#a56060 40%,#3e3b3e 100%)}
.event-card{left:682px;top:219px;width:334px;height:269px;background:var(--white);box-shadow:0 10px 30px rgba(0,0,0,.06);padding:26px 30px}
.meta{font-size:11px;color:var(--muted);display:flex;justify-content:space-between}
.meta b{color:var(--dark);font-weight:400}
.event-card h3{margin-top:14px;font-size:18px;line-height:27px;font-weight:600}
.event-card p{margin-top:10px;font-size:11px;line-height:20px;color:var(--muted)}
.event-card .learn{justify-content:flex-start;color:var(--gold)}
.event-small{top:557px;width:262px;height:334px;background:var(--white)}
.event-small .thumb{height:181px}
.event-small .body{padding:24px 18px}
.event-small .date{font-size:11px;color:var(--muted)}
.event-small h4{margin-top:16px;font-size:15px;line-height:22px;font-weight:600}
.event-small .learn{justify-content:flex-start;color:var(--peach)}

/* testimonials */
.reviews{top:3314px;height:777px}
.reviews .section-title{top:92px}
.review-photo{left:184px;top:207px;width:404px;height:482px;background:linear-gradient(160deg,#e9e7e4 0%,#c9c3bb 50%,#8d8580 100%)}
.play{left:537px;top:402px;width:90px;height:90px;border-radius:50%;background:var(--white);box-shadow:0 8px 24px rgba(0,0,0,.12);display:flex;align-items:center;justify-content:center}
.stars{left:666px;top:248px;display:flex;gap:3px}
.reviews h3{position:absolute;left:666px;top:290px;font-size:22px}
.reviews .quote{position:absolute;left:666px;top:343px;width:340px;font-size:13px;line-height:25px;color:var(--muted)}
.reviews .name{position:absolute;left:666px;top:530px;font-size:18px}
.reviews .role{position:absolute;left:666px;top:563px;font-size:13px;color:var(--muted)}
.avatars{left:666px;top:615px;display:flex}
.avatars span{width:38px;height:38px;border-radius:50%;border:2px solid var(--white);background:linear-gradient(160deg,#a79a90,#5d5550);margin-right:-8px}

/* tips & contact */
.tips{top:4091px;height:449px;background:linear-gradient(180deg,#5e6f6e 0%,#4e615f 60%,#44575a 100%)}
.tips h2{position:absolute;top:118px;left:0;width:1200px;text-align:center;color:var(--white);font-size:34px}
.tips p{position:absolute;top:186px;left:300px;width:600px;text-align:center;color:var(--white);font-size:13px;line-height:25px}
.contact-panel{left:232px;top:4364px;width:784px;height:574px;background:var(--white);box-shadow:0 10px 40px rgba(0,0,0,.08);display:flex}
.contact-info{width:286px;background:var(--cream);padding:108px 0 0 36px}
.contact-info h3{font-size:17px;color:var(--gold)}
.info-row{display:flex;gap:14px;margin-top:28px;font-size:13px;line-height:22px}
.info-row svg{flex:none;margin-top:3px}
.contact-form{flex:1;padding:68px 70px 0 50px}
.contact-form h3{font-size:20px}
.contact-form .sub{margin-top:14px;font-size:11px;line-height:20px;color:var(--muted);width:310px}
.field-row{display:flex;gap:40px;margin-top:34px}
.field{flex:1;border-bottom:1px solid var(--line);padding-bottom:14px;font-size:10px;color:var(--muted)}
.send{position:relative;margin-top:110px;width:156px;height:58px}

/* footer */
.site-footer{top:5025px;height:347px;background:var(--dark);color:var(--white)}
.foot-brand{left:244px;top:72px;width:142px;display:flex;flex-direction:column;align-items:center;gap:8px}
.foot-brand .brand-name{color:var(--white)}
.foot-brand .brand-mark{background:var(--white)}
.foot-about{left:214px;top:156px;width:200px;text-align:center;font-size:10px;line-height:19px}
.foot-col{top:88px;font-size:14px}
.foot-links{top:156px;font-size:10px;line-height:22px}
.subscribe{left:753px;top:163px;width:230px;height:50px;border-radius:30px;background:var(--white);display:flex;align-items:center;justify-content:space-between;padding:0 4px 0 24px;font-size:9px;color:var(--muted)}
.subscribe span.go{width:42px;height:42px;border-radius:50%;background:var(--green);display:flex;align-items:center;justify-content:center}
.socials{left:761px;top:239px;display:flex;gap:22px}
.socials span{width:12px;height:12px;border-radius:50%;background:var(--white)}
.copyright{top:5344px;left:0;width:1200px;text-align:center;font-size:10px;color:var(--white)}
</style>
</head>
<body>

<header class="site-header">
  <div class="abs brand"><span class="brand-name">EVERBLOOM</span><span class="brand-mark"></span></div>
  <span class="abs nav active" style="left:442px">Home</span>
  <span class="abs nav" style="left:532px">About Us</span>
  <span class="abs nav" style="left:641px">Resources</span>
  <span class="abs nav" style="left:760px">Coaching &amp; Counselling</span>
  <span class="abs nav" style="left:964px">Contact</span>
</header>

<section class="hero" role="img" aria-label="Woman with raised arms standing in the sea at sunset">
  <h1>Holistic Transformational<br>Coaching</h1>
  <p>Lorem ipsum dolor sit amet, consectetur adipiscing elit, sed do eiusmod tempor incididunt ut labore et dolore magna aliqua. Ut enim ad minim veniam, quis nostrud exercitation ullamco laboris.</p>
  <span class="btn" style="left:434px;top:320px;width:129px">Read More</span>
  <span class="btn btn-ghost" style="left:595px;top:320px;width:169px">Watch Video
    <svg width="18" height="18" viewBox="0 0 18 18"><circle cx="9" cy="9" r="9" fill="#fff"/><path d="M7 5.5l5 3.5-5 3.5z" fill="#c9772a"/></svg></span>
</section>

<div class="abs partners">
  <span class="partner">Northlane</span>
  <span class="partner-sq"></span>
  <span class="partner">Cedarwell</span>
  <span class="partner">Stonefield</span>
  <span class="partner-sq"></span>
  <span class="partner-sq"></span>
  <span class="partner-sq"></span>
  <span class="partner">Mapleford</span>
  <span class="partner">Brightmoor</span>
</div>

<section class="about">
  <div class="abs about-frame"></div>
  <div class="abs about-photo" role="img" aria-label="Portrait of the coach in a white shirt and grey skirt"></div>
  <h2 class="abs">About Us</h2>
  <p class="abs lead">Calm Ridge Mentoring by Master Life Coach Marisol Keane is based in Newcastle, Australia.</p>
  <p class="abs body">Have you started numerous weight loss challenges, get fit quick programs, university degrees or small business but somehow end up quitting over and over again? Do you promise yourself that this time you will stick to it? Or are you just feeling stuck in life and need direction.</p>
  <span class="btn" style="left:611px;top:426px;width:132px">Read More</span>
</section>

<section class="booking" role="img" aria-label="Two people in a coaching session at a table">
  <p>Book a 30minute complimentary session with brenna to discuss your requirments in details.</p>
  <span class="btn" style="left:501px;top:193px;width:198px">Get An Appointment</span>
</section>

<section class="services">
  <h2 class="section-title">Our Services</h2>
  <p class="intro">Lorem ipsum dolor sit amet, consectetur adipiscing elit, sed do eiusmod tempor incididunt ut labore et dolore magna aliqua.</p>
  <span class="arrow-btn off" style="left:918px;top:149px"><svg width="14" height="10" viewBox="0 0 14 10"><path d="M13 5H1M5 1L1 5l4 4" stroke="#ccc" fill="none" stroke-width="1.4"/></svg></span>
  <span class="arrow-btn on" style="left:979px;top:149px"><svg width="14" height="10" viewBox="0 0 14 10"><path d="M1 5h12M9 1l4 4-4 4" stroke="#fff" fill="none" stroke-width="1.4"/></svg></span>

  <div class="service-card" style="left:184px">
    <div class="thumb" role="img" aria-label="Woman in a sunflower field with bubbles" style="background:linear-gradient(180deg,#8fb8d8 0%,#e8c04a 55%,#4c6b2e 100%)"></div>
    <h3>What I Do</h3>
    <p>Lorem ipsum dolor sit amet, consectetur adipiscing elit, sed do eiusmod tempor incididunt.</p>
    <div class="learn">Learn More →</div>
  </div>
  <div class="service-card" style="left:469px">
    <div class="thumb" role="img" aria-label="Coach and client seated in a bright room" style="background:linear-gradient(180deg,#ecebe8 0%,#c9c4bc 60%,#6f6760 100%)"></div>
    <h3>Coaching &amp; Counselling</h3>
    <p>Lorem ipsum dolor sit amet, consectetur adipiscing elit, sed do eiusmod tempor incididunt.</p>
    <div class="learn on">Learn More →</div>
  </div>
  <div class="service-card" style="left:754px">
    <div class="thumb" role="img" aria-label="Team working around a table seen from above" style="background:linear-gradient(160deg,#d9d6d0 0%,#8a6a4e 50%,#3f3a36 100%)"></div>
    <h3>Workshop</h3>
    <p>Lorem ipsum dolor sit amet, consectetur adipiscing elit, sed do eiusmod tempor incididunt.</p>
    <div class="learn">Learn More →</div>
  </div>
</section>

<section class="events">
  <h2 class="section-title center">Upcoming Event</h2>
  <div class="abs event-feature" role="img" aria-label="Speaker presenting to a full lecture hall"></div>
  <div class="abs event-card">
    <div class="meta"><span>Post by - <b>John Doe</b></span><span>10/04/2021</span></div>
    <h3>Lorem ipsum dolor sit amet consectetur adipiscing elit</h3>
    <p>Lorem ipsum dolor sit amet, consectetur adipiscing elit, sed do eiusmod tempor incididunt ut labore et dolore magna aliqua. Quis ipsum suspendisse.</p>
    <div class="learn">Read More →</div>
  </div>
  <span class="arrow-btn" style="left:100px;top:523px;background:#fff"><svg width="14" height="10" viewBox="0 0 14 10"><path d="M13 5H1M5 1L1 5l4 4" stroke="#ccc" fill="none" stroke-width="1.4"/></svg></span>
  <span class="arrow-btn on" style="left:1060px;top:523px"><svg width="14" height="10" viewBox="0 0 14 10"><path d="M1 5h12M9 1l4 4-4 4" stroke="#fff" fill="none" stroke-width="1.4"/></svg></span>

  <div class="abs event-small" style="left:184px">
    <div class="thumb" role="img" aria-label="Speaker at a lectern" style="background:linear-gradient(180deg,#d6d3cd 0%,#8d8680 60%,#3c3a3a 100%)"></div>
    <div class="body"><div class="date">Date - 15/04/2021</div><h4>Simply dummy text of the printing and typesetting.</h4><div class="learn">Read More →</div></div>
  </div>
  <div class="abs event-small" style="left:469px">
    <div class="thumb" role="img" aria-label="Presentation screen in a dim conference room" style="background:linear-gradient(180deg,#6a4f6f 0%,#b8765a 55%,#3a2e2e 100%)"></div>
    <div class="body"><div class="date">Date - 28/04/2021</div><h4>Simply dummy text of the printing and typesetting.</h4><div class="learn">Read More →</div></div>
  </div>
  <div class="abs event-small" style="left:754px">
    <div class="thumb" role="img" aria-label="Speaker gesturing on stage" style="background:linear-gradient(180deg,#5b5f66 0%,#8b8a8c 50%,#2f3033 100%)"></div>
    <div class="body"><div class="date">Date - 02/05/2021</div><h4>Simply dummy text of the printing and typesetting.</h4><div class="learn">Read More →</div></div>
  </div>
</section>

<section class="reviews">
  <h2 class="section-title center">People say the nicest things</h2>
  <div class="abs review-photo" role="img" aria-label="Portrait of a smiling client in a white t-shirt"></div>
  <div class="abs play"><svg width="22" height="24" viewBox="0 0 22 24"><path d="M2 1l19 11L2 23z" fill="#7EB492"/></svg></div>
  <div class="abs stars">
    <svg width="80" height="14" viewBox="0 0 80 14"><g fill="#CAAD53"><path id="st" d="M7 0l2 4.6 5 .4-3.8 3.3 1.2 4.9L7 10.6 2.6 13.2l1.2-4.9L0 5l5-.4z"/><use href="#st" x="16"/><use href="#st" x="32"/><use href="#st" x="48"/><use href="#st" x="64"/></g></svg>
  </div>
  <h3>“ Great Service ”</h3>
  <p class="quote">Lorem ipsum dolor sit amet, consectetur adipiscing elit, sed do eiusmod tempor incididunt ut labore et dolore magna aliqua. Ut enim ad minim veniam, quis nostrud exercitation ullamco laboris nisi ut aliquip ex ea commodo consequat. Duis aute irure dolor in reprehenderit in voluptate velit esse cillum dolore eu fugiat.</p>
  <div class="name">John Doe</div>
  <div class="role">Funder of Lorem</div>
  <div class="abs avatars" role="img" aria-label="Other client portraits"><span></span><span></span><span></span></div>
</section>

<section class="tips" role="img" aria-label="Person with raised arms against a misty sky">
  <h2>7 Tips to make you feel appreciated again Today!</h2>
  <p>Lorem ipsum dolor sit amet, consectetur adipiscing elit, sed do eiusmod tempor incididunt ut labore et dolore magna aliqua.</p>
</section>

<div class="abs contact-panel">
  <div class="contact-info">
    <h3>Contact Information</h3>
    <div class="info-row" style="margin-top:38px">
      <svg width="14" height="16" viewBox="0 0 14 16"><path d="M7 15s5-5 5-9A5 5 0 0 0 2 6c0 4 5 9 5 9z" fill="none" stroke="#7EB492" stroke-width="1.3"/><circle cx="7" cy="6" r="1.8" fill="#7EB492"/></svg>
      <div>18 Lantern Row,<br>Harbourside - 400210,<br><br>2207 Cedar Vale Ave P.O.<br>Box 118804 Alder Bay,<br>CA 90411</div>
    </div>
    <div class="info-row">
      <svg width="14" height="14" viewBox="0 0 14 14"><path d="M3 1l2.5 3-1.5 1.5a8 8 0 0 0 4.5 4.5L10 8.5l3 2.5-1.5 2C6 13 1 8 1 2.5z" fill="none" stroke="#7EB492" stroke-width="1.2"/></svg>
      <div>+987 650 11224<br>+614 150 22719</div>
    </div>
    <div class="info-row">
      <svg width="15" height="12" viewBox="0 0 15 12"><rect x=".6" y=".6" width="13.8" height="10.8" fill="none" stroke="#7EB492" stroke-width="1.2"/><path d="M1 1l6.5 5.5L14 1" fill="none" stroke="#7EB492" stroke-width="1.2"/></svg>
      <div>brenna@brennaolstead.co<br>marisol@calmridgementoring<br>.com.au</div>
    </div>
    <div class="info-row">
      <svg width="14" height="14" viewBox="0 0 14 14"><rect x=".6" y=".6" width="12.8" height="12.8" rx="3" fill="none" stroke="#7EB492" stroke-width="1.2"/></svg>
      <div>John.Doe 0123</div>
    </div>
  </div>
  <div class="contact-form">
    <h3>Get In Touch</h3>
    <p class="sub">Lorem ipsum dolor sit amet consectetur adipiscing elit sed do eiusmod tempor incididunt.</p>
    <div class="field-row"><span class="field">First Name</span><span class="field">Last Name</span></div>
    <div class="field-row"><span class="field">Enter Your Email Id</span></div>
    <div class="field-row"><span class="field">Phone Number</span><span class="field">Subject</span></div>
    <div class="field-row"><span class="field" style="border:0">Type a message...</span></div>
    <span class="btn send">Send Message</span>
  </div>
</div>

<footer class="site-footer">
  <div class="abs foot-brand"><span class="brand-name">EVERBLOOM</span><span class="brand-mark"></span></div>
  <p class="abs foot-about">Lorem ipsum dolor sit amet, consectetur adipiscing elit, sed do eiusmod tempor incididunt ut labore et dolore magna aliqua.</p>
  <span class="abs foot-col" style="left:467px">The Work</span>
  <span class="abs foot-col" style="left:609px">Our Service</span>
  <span class="abs foot-col" style="left:753px">Subscribe</span>
  <div class="abs foot-links" style="left:467px">How to do The Work<br>Videos<br>FAQs<br>Certified Facilitators<br>Resources<br>Guided Meditation</div>
  <div class="abs foot-links" style="left:609px">Books<br>About<br>Press Kit<br>In the Media<br>Ines Harrow's Blog<br>Invitations</div>
  <div class="abs subscribe"><span>Enter Your Email</span><span class="go"><svg width="16" height="16" viewBox="0 0 16 16"><path d="M2 8l12-6-4 12-2-5z" fill="none" stroke="#fff" stroke-width="1.3"/></svg></span></div>
  <div class="abs socials"><span></span><span></span><span></span><span></span></div>
</footer>
<div class="abs copyright">© copyright@ 2021 everbloom.com</div>

</body>
</html>
```